Hotel Company Personal Business Card

This is a hotel business, personal business card. Need it sleek, professional, and sharp looking. I have a design attached that we can work with. My turnaround time is April 8th. I would need the cards by then. One side only color, the other side all details. This is flexible depending on the designs you come up with. I would like a boutique, unique, modern type of touch to the business card. Memorable type of card that people will want to keep.

Target Market(s)

Business professionals

Industry/Entity Type

Hospitality/Hotels & Resorts

Contact Information for Business Card

Name, email, phone number, address, and company name. Anything unique

Font styles to use
Serif
Sans Serif

Colors

Designer to choose colors to be used in the design.

Requirements
Nice to have
• Neutral colors. Eye popping logo. Sleek design. Boutique feel. Hint of color.

```html
<!DOCTYPE html>
<html lang="en">
<head>
<meta charset="utf-8">
<title>Alder House – Business Card</title>
<link href="https://fonts.googleapis.com/css2?family=Montserrat:wght@400;500&family=Lato:wght@400&display=swap" rel="stylesheet">
<style>
  :root{
    --backdrop:#aea79d;
    --card-back:#4f3b1f;
    --card-back-pattern:#5d4829;
    --card-front:#5e4e35;
    --ornament:#7a6544;
    --gold:#8f7851;
    --ink:#ffffff;
  }
  *{margin:0;padding:0;box-sizing:border-box}
  html,body{width:1200px;height:1000px;overflow:hidden;background:var(--backdrop)}
  .stage{position:relative;width:1200px;height:1000px}
  .card{position:absolute;left:196px;width:808px;height:462px;border-radius:0 18px 0 18px;overflow:hidden}
  .card--back{top:30px;background:var(--card-back)}
  .card--back .pattern-fill{position:absolute;inset:0;background:radial-gradient(circle at 50% 50%,var(--card-back-pattern),var(--card-back) 80%)}
  .card--front{top:508px;background:var(--card-front)}
  .brand{position:absolute;left:48px;top:42px;display:flex;align-items:center;gap:10px;
    font-family:"Montserrat",sans-serif;font-weight:500;font-size:22px;letter-spacing:3px;color:var(--gold)}
  .brand__dot{width:12px;height:12px;background:var(--gold)}
  .identity{position:absolute;left:482px;top:30px;color:var(--ink);font-family:"Montserrat",sans-serif;white-space:nowrap}
  .identity__name{font-size:40px;font-weight:400;letter-spacing:1px;line-height:1.2}
  .identity__role{font-size:20px;font-weight:500;margin-top:2px;margin-left:2px}
  .contact{position:absolute;left:46px;top:256px;list-style:none;font-family:"Lato",sans-serif;font-size:21px;color:var(--ink)}
  .contact li{display:flex;align-items:flex-start;gap:10px;line-height:26px;margin-bottom:7px}
  .contact svg{flex:none;margin-top:5px}
  .ornament{position:absolute;right:0;bottom:0;width:430px;height:462px}
  .border-band{position:absolute;left:0;bottom:0;width:400px;height:62px;
    background:linear-gradient(to bottom,rgba(143,120,81,.55),rgba(122,101,68,.35))}
</style>
</head>
<body>
<div class="stage">
  <section class="card card--back">
    <div class="pattern-fill" role="img" aria-label="All-over paisley pattern in tonal brown"></div>
  </section>

  <section class="card card--front">
    <div class="brand"><span class="brand__dot"></span>ALDER HOUSE</div>

    <div class="identity">
      <div class="identity__name">AARON SILVA</div>
      <div class="identity__role">CEO</div>
    </div>

    <ul class="contact">
      <li>
        <svg width="16" height="16" viewBox="0 0 16 16"><path d="M3 1l3 3-2 2c1 2 3 4 5 5l2-2 3 3-2 3C6 14 1 9 1 3z" fill="#fff"/></svg>
        044-555 012 348
      </li>
      <li>
        <svg width="16" height="16" viewBox="0 0 16 16"><path d="M1 8l14-6-5 13-2-5z" fill="#fff"/></svg>
        stay@alderhouse.com
      </li>
      <li>
        <svg width="16" height="18" viewBox="0 0 16 18"><path d="M8 1a6 6 0 0 0-6 6c0 4 6 10 6 10s6-6 6-10a6 6 0 0 0-6-6z" fill="#fff"/><circle cx="8" cy="7" r="2.2" fill="#5e4e35"/></svg>
        <span>4721 Harbor Light Blvd,<br>210-B, FL 32401</span>
      </li>
    </ul>

    <svg class="ornament" viewBox="0 0 430 462" role="img" aria-label="Corner mandala ornament in muted gold line work">
      <defs>
        <radialGradient id="ornamentTone" cx="85%" cy="90%" r="80%">
          <stop offset="0" stop-color="#7a6544" stop-opacity=".55"/>
          <stop offset="1" stop-color="#7a6544" stop-opacity="0"/>
        </radialGradient>
      </defs>
      <path d="M430 0 V462 H30 C60 400 120 330 190 300 C240 250 300 170 360 120 C400 80 420 40 430 0z" fill="url(#ornamentTone)"/>
    </svg>

    <div class="border-band" role="img" aria-label="Decorative triangle and scallop border in muted gold"></div>
  </section>
</div>
</body>
</html>
```